We are looking to create a graphic that will be used in Facebook posts each week to show the daily Porchlight Report. Attached is an example of what we are looking for. We need to be able to update the forecast. So we will need hi-res vector files. The graphics need to represent the level of mosquito activity: SLIGHT, AVERAGE, INTENSE, EXTREME

```html
<!DOCTYPE html>
<html lang="en">
<head>
<meta charset="utf-8">
<title>Porchlight Report – Weekly Activity Graphic</title>
<link rel="stylesheet" href="https://fonts.googleapis.com/css2?family=Catamaran:wght@700&family=Montserrat:wght@600&family=Playfair+Display:wght@700&family=Poppins:wght@400&family=Fira+Sans:wght@400;500;700&display=swap">
<style>
  :root {
    --page-bg: #d6d7d8;
    --band-bg: #e3e4e5;
    --heading: #1c2a10;
    --subheading: #0f3d20;
    --panel: #ffffff;
    --ink: #1a1a1a;
    --muted: #555555;
    --rule: #bdbdbd;
    --track: #e2e2e2;
    --slight: #3a8c12;
    --average: #f9b800;
    --intense: #f55a1f;
    --extreme: #b0101a;
  }
  * { margin: 0; padding: 0; box-sizing: border-box; }
  html, body { width: 1200px; height: 781px; overflow: hidden; }
  body {
    position: relative;
    background: linear-gradient(180deg, #d2d3d4 0%, #dcdddd 100%);
    font-family: "Fira Sans", sans-serif;
    color: var(--ink);
  }
  .page-title {
    position: absolute; top: 46px; left: 0; width: 1200px;
    text-align: center;
    font-family: "Catamaran", sans-serif; font-weight: 700;
    font-size: 60px; line-height: 70px; color: var(--heading);
  }
  .revision-band {
    position: absolute; top: 134px; left: 0; width: 1200px; height: 58px;
    background: var(--band-bg);
    display: flex; align-items: center; justify-content: center;
    font-family: "Montserrat", sans-serif; font-weight: 600;
    font-size: 26px; color: var(--subheading); letter-spacing: 0.5px;
  }
  .graphic {
    position: absolute; top: 216px; left: 87px; width: 1051px; height: 552px;
    overflow: hidden;
  }
  .graphic-photo {
    position: absolute; inset: 0;
    background:
      linear-gradient(180deg, rgba(120,135,140,0.55) 0%, rgba(60,70,60,0.35) 30%, rgba(40,60,30,0) 55%),
      linear-gradient(180deg, #9fb0b4 0%, #5c6458 25%, #3d4a36 48%, #2f5a1e 70%, #3f7a22 100%);
  }
  .graphic-title {
    position: absolute; top: 92px; left: 0; width: 100%;
    text-align: center;
    font-family: "Playfair Display", serif; font-weight: 700;
    font-size: 70px; line-height: 76px; color: #ffffff;
    letter-spacing: -1px;
  }
  .graphic-region {
    position: absolute; top: 156px; left: 0; width: 100%;
    text-align: center;
    font-family: "Poppins", sans-serif; font-weight: 400;
    font-size: 40px; line-height: 52px; color: #ffffff;
  }
  .forecast-panel {
    position: absolute; top: 230px; left: 18px; width: 1013px; height: 285px;
    background: var(--panel);
  }
  .day {
    position: absolute; top: 0; width: 142px; text-align: center;
  }
  .day-name { position: absolute; top: 39px; width: 100%; font-size: 12px; font-weight: 500; }
  .day-date { position: absolute; top: 58px; width: 100%; font-size: 10px; color: var(--muted); }
  .gauge { position: absolute; top: 87px; left: 15px; width: 112px; height: 112px; }
  .level-badge {
    position: absolute; top: 193px; left: 40px; width: 62px; height: 17px;
    font-size: 8px; font-weight: 700; letter-spacing: 0.4px;
    color: #fff; line-height: 17px; text-align: center;
  }
  .divider { position: absolute; top: 55px; width: 1px; height: 184px; background: var(--rule); }
  .baseline { position: absolute; top: 240px; left: 35px; width: 958px; height: 1px; background: var(--rule); }
  .legend { position: absolute; top: 252px; left: 0; width: 100%; height: 14px; }
  .legend-swatch { position: absolute; top: 0; width: 45px; height: 13px; }
  .legend-label { position: absolute; top: 0; font-size: 9.5px; line-height: 13px; color: var(--ink); }
  .is-slight { background: var(--slight); }
  .is-average { background: var(--average); }
  .is-intense { background: var(--intense); }
  .is-extreme { background: var(--extreme); }
  .seg { fill: none; stroke-width: 12; }
</style>
</head>
<body>
  <h1 class="page-title">Porchlight Report</h1>
  <div class="revision-band">Revision 2- Mockup 3b</div>

  <section class="graphic">
    <div class="graphic-photo" role="img" aria-label="Blurred photo of a dark house behind tall green grass"></div>
    <h2 class="graphic-title">PORCHLIGHT REPORT</h2>
    <p class="graphic-region">Greater Milwakukee</p>

    <div class="forecast-panel">
      <svg width="0" height="0" style="position:absolute">
        <defs>
          <g id="gauge-frame">
            <path d="M21.11 98.89 A55 55 0 1 1 98.89 98.89 L86.87 86.87 A38 38 0 1 0 33.13 86.87 Z" fill="#fff" stroke="#222" stroke-width="1"/>
          </g>
        </defs>
      </svg>

      <!-- Monday: slight -->
      <div class="day" style="left:10px">
        <div class="day-name">Mon Day</div><div class="day-date">02/20</div>
        <svg class="gauge" viewBox="0 0 120 120">
          <use href="#gauge-frame"/>
          <g transform="rotate(135 60 60)">
            <circle class="seg" cx="60" cy="60" r="47" pathLength="360" stroke-dasharray="31.75 328.25" stroke-dashoffset="-1" stroke="var(--slight)"/>
            <circle class="seg" cx="60" cy="60" r="47" pathLength="360" stroke-dasharray="31.75 328.25" stroke-dashoffset="-34.75" stroke="var(--slight)"/>
            <circle class="seg" cx="60" cy="60" r="47" pathLength="360" stroke-dasharray="31.75 328.25" stroke-dashoffset="-68.5" stroke="var(--track)"/>
            <circle class="seg" cx="60" cy="60" r="47" pathLength="360" stroke-dasharray="31.75 328.25" stroke-dashoffset="-102.25" stroke="var(--track)"/>
            <circle class="seg" cx="60" cy="60" r="47" pathLength="360" stroke-dasharray="31.75 328.25" stroke-dashoffset="-136" stroke="var(--track)"/>
            <circle class="seg" cx="60" cy="60" r="47" pathLength="360" stroke-dasharray="31.75 328.25" stroke-dashoffset="-169.75" stroke="var(--track)"/>
            <circle class="seg" cx="60" cy="60" r="47" pathLength="360" stroke-dasharray="31.75 328.25" stroke-dashoffset="-203.5" stroke="var(--track)"/>
            <circle class="seg" cx="60" cy="60" r="47" pathLength="360" stroke-dasharray="31.75 328.25" stroke-dashoffset="-237.25" stroke="var(--track)"/>
          </g>
          <circle cx="60" cy="60" r="35" fill="#fff" stroke="#222" stroke-width="1"/>
          <circle cx="60" cy="60" r="29" fill="var(--slight)"/>
        </svg>
        <div class="level-badge is-slight">SLIGHT</div>
      </div>
      <div class="divider" style="left:156px"></div>

      <!-- Tuesday: average -->
      <div class="day" style="left:152px">
        <div class="day-name">Tues Day</div><div class="day-date">02/21</div>
        <svg class="gauge" viewBox="0 0 120 120">
          <use href="#gauge-frame"/>
          <g transform="rotate(135 60 60)">
            <circle class="seg" cx="60" cy="60" r="47" pathLength="360" stroke-dasharray="31.75 328.25" stroke-dashoffset="-1" stroke="var(--slight)"/>
            <circle class="seg" cx="60" cy="60" r="47" pathLength="360" stroke-dasharray="31.75 328.25" stroke-dashoffset="-34.75" stroke="var(--slight)"/>
            <circle class="seg" cx="60" cy="60" r="47" pathLength="360" stroke-dasharray="31.75 328.25" stroke-dashoffset="-68.5" stroke="var(--average)"/>
            <circle class="seg" cx="60" cy="60" r="47" pathLength="360" stroke-dasharray="31.75 328.25" stroke-dashoffset="-102.25" stroke="var(--average)"/>
            <circle class="seg" cx="60" cy="60" r="47" pathLength="360" stroke-dasharray="31.75 328.25" stroke-dashoffset="-136" stroke="var(--track)"/>
            <circle class="seg" cx="60" cy="60" r="47" pathLength="360" stroke-dasharray="31.75 328.25" stroke-dashoffset="-169.75" stroke="var(--track)"/>
            <circle class="seg" cx="60" cy="60" r="47" pathLength="360" stroke-dasharray="31.75 328.25" stroke-dashoffset="-203.5" stroke="var(--track)"/>
            <circle class="seg" cx="60" cy="60" r="47" pathLength="360" stroke-dasharray="31.75 328.25" stroke-dashoffset="-237.25" stroke="var(--track)"/>
          </g>
          <circle cx="60" cy="60" r="35" fill="#fff" stroke="#222" stroke-width="1"/>
          <circle cx="60" cy="60" r="29" fill="var(--average)"/>
        </svg>
        <div class="level-badge is-average">AVERAGE</div>
      </div>
      <div class="divider" style="left:297px"></div>

      <!-- Wednesday: intense -->
      <div class="day" style="left:294px">
        <div class="day-name">Wednes Day</div><div class="day-date">02/22</div>
        <svg class="gauge" viewBox="0 0 120 120">
          <use href="#gauge-frame"/>
          <g transform="rotate(135 60 60)">
            <circle class="seg" cx="60" cy="60" r="47" pathLength="360" stroke-dasharray="31.75 328.25" stroke-dashoffset="-1" stroke="var(--slight)"/>
            <circle class="seg" cx="60" cy="60" r="47" pathLength="360" stroke-dasharray="31.75 328.25" stroke-dashoffset="-34.75" stroke="var(--slight)"/>
            <circle class="seg" cx="60" cy="60" r="47" pathLength="360" stroke-dasharray="31.75 328.25" stroke-dashoffset="-68.5" stroke="var(--average)"/>
            <circle class="seg" cx="60" cy="60" r="47" pathLength="360" stroke-dasharray="31.75 328.25" stroke-dashoffset="-102.25" stroke="var(--average)"/>
            <circle class="seg" cx="60" cy="60" r="47" pathLength="360" stroke-dasharray="31.75 328.25" stroke-dashoffset="-136" stroke="var(--intense)"/>
            <circle class="seg" cx="60" cy="60" r="47" pathLength="360" stroke-dasharray="31.75 328.25" stroke-dashoffset="-169.75" stroke="var(--intense)"/>
            <circle class="seg" cx="60" cy="60" r="47" pathLength="360" stroke-dasharray="31.75 328.25" stroke-dashoffset="-203.5" stroke="var(--track)"/>
            <circle class="seg" cx="60" cy="60" r="47" pathLength="360" stroke-dasharray="31.75 328.25" stroke-dashoffset="-237.25" stroke="var(--track)"/>
          </g>
          <circle cx="60" cy="60" r="35" fill="#fff" stroke="#222" stroke-width="1"/>
          <circle cx="60" cy="60" r="29" fill="var(--intense)"/>
        </svg>
        <div class="level-badge is-intense">INTENSE</div>
      </div>
      <div class="divider" style="left:437px"></div>

      <!-- Thursday: extreme -->
      <div class="day" style="left:436px">
        <div class="day-name">Thurs Day</div><div class="day-date">02/23</div>
        <svg class="gauge" viewBox="0 0 120 120">
          <use href="#gauge-frame"/>
          <g transform="rotate(135 60 60)">
            <circle class="seg" cx="60" cy="60" r="47" pathLength="360" stroke-dasharray="31.75 328.25" stroke-dashoffset="-1" stroke="var(--slight)"/>
            <circle class="seg" cx="60" cy="60" r="47" pathLength="360" stroke-dasharray="31.75 328.25" stroke-dashoffset="-34.75" stroke="var(--slight)"/>
            <circle class="seg" cx="60" cy="60" r="47" pathLength="360" stroke-dasharray="31.75 328.25" stroke-dashoffset="-68.5" stroke="var(--average)"/>
            <circle class="seg" cx="60" cy="60" r="47" pathLength="360" stroke-dasharray="31.75 328.25" stroke-dashoffset="-102.25" stroke="var(--average)"/>
            <circle class="seg" cx="60" cy="60" r="47" pathLength="360" stroke-dasharray="31.75 328.25" stroke-dashoffset="-136" stroke="var(--intense)"/>
            <circle class="seg" cx="60" cy="60" r="47" pathLength="360" stroke-dasharray="31.75 328.25" stroke-dashoffset="-169.75" stroke="var(--intense)"/>
            <circle class="seg" cx="60" cy="60" r="47" pathLength="360" stroke-dasharray="31.75 328.25" stroke-dashoffset="-203.5" stroke="var(--extreme)"/>
            <circle class="seg" cx="60" cy="60" r="47" pathLength="360" stroke-dasharray="31.75 328.25" stroke-dashoffset="-237.25" stroke="var(--extreme)"/>
          </g>
          <circle cx="60" cy="60" r="35" fill="#fff" stroke="#222" stroke-width="1"/>
          <circle cx="60" cy="60" r="29" fill="var(--extreme)"/>
        </svg>
        <div class="level-badge is-extreme">EXTREME</div>
      </div>
      <div class="divider" style="left:578px"></div>

      <!-- Friday: average -->
      <div class="day" style="left:578px">
        <div class="day-name">Fri Day</div><div class="day-date">02/24</div>
        <svg class="gauge" viewBox="0 0 120 120">
          <use href="#gauge-frame"/>
          <g transform="rotate(135 60 60)">
            <circle class="seg" cx="60" cy="60" r="47" pathLength="360" stroke-dasharray="31.75 328.25" stroke-dashoffset="-1" stroke="var(--slight)"/>
            <circle class="seg" cx="60" cy="60" r="47" pathLength="360" stroke-dasharray="31.75 328.25" stroke-dashoffset="-34.75" stroke="var(--slight)"/>
            <circle class="seg" cx="60" cy="60" r="47" pathLength="360" stroke-dasharray="31.75 328.25" stroke-dashoffset="-68.5" stroke="var(--average)"/>
            <circle class="seg" cx="60" cy="60" r="47" pathLength="360" stroke-dasharray="31.75 328.25" stroke-dashoffset="-102.25" stroke="var(--average)"/>
            <circle class="seg" cx="60" cy="60" r="47" pathLength="360" stroke-dasharray="31.75 328.25" stroke-dashoffset="-136" stroke="var(--track)"/>
            <circle class="seg" cx="60" cy="60" r="47" pathLength="360" stroke-dasharray="31.75 328.25" stroke-dashoffset="-169.75" stroke="var(--track)"/>
            <circle class="seg" cx="60" cy="60" r="47" pathLength="360" stroke-dasharray="31.75 328.25" stroke-dashoffset="-203.5" stroke="var(--track)"/>
            <circle class="seg" cx="60" cy="60" r="47" pathLength="360" stroke-dasharray="31.75 328.25" stroke-dashoffset="-237.25" stroke="var(--track)"/>
          </g>
          <circle cx="60" cy="60" r="35" fill="#fff" stroke="#222" stroke-width="1"/>
          <circle cx="60" cy="60" r="29" fill="var(--average)"/>
        </svg>
        <div class="level-badge is-average">AVERAGE</div>
      </div>
      <div class="divider" style="left:719px"></div>

      <!-- Saturday: intense -->
      <div class="day" style="left:720px">
        <div class="day-name">Satur Day</div><div class="day-date">02/25</div>
        <svg class="gauge" viewBox="0 0 120 120">
          <use href="#gauge-frame"/>
          <g transform="rotate(135 60 60)">
            <circle class="seg" cx="60" cy="60" r="47" pathLength="360" stroke-dasharray="31.75 328.25" stroke-dashoffset="-1" stroke="var(--slight)"/>
            <circle class="seg" cx="60" cy="60" r="47" pathLength="360" stroke-dasharray="31.75 328.25" stroke-dashoffset="-34.75" stroke="var(--slight)"/>
            <circle class="seg" cx="60" cy="60" r="47" pathLength="360" stroke-dasharray="31.75 328.25" stroke-dashoffset="-68.5" stroke="var(--average)"/>
            <circle class="seg" cx="60" cy="60" r="47" pathLength="360" stroke-dasharray="31.75 328.25" stroke-dashoffset="-102.25" stroke="var(--average)"/>
            <circle class="seg" cx="60" cy="60" r="47" pathLength="360" stroke-dasharray="31.75 328.25" stroke-dashoffset="-136" stroke="var(--intense)"/>
            <circle class="seg" cx="60" cy="60" r="47" pathLength="360" stroke-dasharray="31.75 328.25" stroke-dashoffset="-169.75" stroke="var(--intense)"/>
            <circle class="seg" cx="60" cy="60" r="47" pathLength="360" stroke-dasharray="31.75 328.25" stroke-dashoffset="-203.5" stroke="var(--track)"/>
            <circle class="seg" cx="60" cy="60" r="47" pathLength="360" stroke-dasharray="31.75 328.25" stroke-dashoffset="-237.25" stroke="var(--track)"/>
          </g>
          <circle cx="60" cy="60" r="35" fill="#fff" stroke="#222" stroke-width="1"/>
          <circle cx="60" cy="60" r="29" fill="#e46d27"/>
        </svg>
        <div class="level-badge is-intense">INTENSE</div>
      </div>
      <div class="divider" style="left:860px"></div>

      <!-- Sunday: slight -->
      <div class="day" style="left:862px">
        <div class="day-name">Sun Day</div><div class="day-date">02/26</div>
        <svg class="gauge" viewBox="0 0 120 120">
          <use href="#gauge-frame"/>
          <g transform="rotate(135 60 60)">
            <circle class="seg" cx="60" cy="60" r="47" pathLength="360" stroke-dasharray="31.75 328.25" stroke-dashoffset="-1" stroke="var(--slight)"/>
            <circle class="seg" cx="60" cy="60" r="47" pathLength="360" stroke-dasharray="31.75 328.25" stroke-dashoffset="-34.75" stroke="var(--slight)"/>
            <circle class="seg" cx="60" cy="60" r="47" pathLength="360" stroke-dasharray="31.75 328.25" stroke-dashoffset="-68.5" stroke="var(--track)"/>
            <circle class="seg" cx="60" cy="60" r="47" pathLength="360" stroke-dasharray="31.75 328.25" stroke-dashoffset="-102.25" stroke="var(--track)"/>
            <circle class="seg" cx="60" cy="60" r="47" pathLength="360" stroke-dasharray="31.75 328.25" stroke-dashoffset="-136" stroke="var(--track)"/>
            <circle class="seg" cx="60" cy="60" r="47" pathLength="360" stroke-dasharray="31.75 328.25" stroke-dashoffset="-169.75" stroke="var(--track)"/>
            <circle class="seg" cx="60" cy="60" r="47" pathLength="360" stroke-dasharray="31.75 328.25" stroke-dashoffset="-203.5" stroke="var(--track)"/>
            <circle class="seg" cx="60" cy="60" r="47" pathLength="360" stroke-dasharray="31.75 328.25" stroke-dashoffset="-237.25" stroke="var(--track)"/>
          </g>
          <circle cx="60" cy="60" r="35" fill="#fff" stroke="#222" stroke-width="1"/>
          <circle cx="60" cy="60" r="29" fill="var(--slight)"/>
        </svg>
        <div class="level-badge is-slight">SLIGHT</div>
      </div>

      <div class="baseline"></div>

      <div class="legend">
        <span class="legend-swatch is-slight" style="left:328px"></span><span class="legend-label" style="left:381px">Slight</span>
        <span class="legend-swatch is-average" style="left:415px"></span><span class="legend-label" style="left:465px">Average</span>
        <span class="legend-swatch is-intense" style="left:509px"></span><span class="legend-label" style="left:559px">Intense</span>
        <span class="legend-swatch is-extreme" style="left:602px"></span><span class="legend-label" style="left:652px">Extreme</span>
      </div>
    </div>
  </section>
</body>
</html>
```